Business Card Design

We need a new buisness card designed for a new company in Darwin
We dig trenchs and lay pipes for the communication industry,Electrical industry, Teleco industry,
We also do some concrete works as well,
And small excavation work
Communication
Belvanti Contracting PTY LTD
Pit and Pipe installations
Trenching,Excavations, Concreting ,
civil works, unistrut soloutions ,over thirty years experiance
WHERE NOT FAZED WE WILL LAY ANYTHING
Contact Glen 0491536208 ps
(would like name to stand out somehow in another text or graphic sort of a way am also looking for some sort of slogan) will most likely be a red card with black writing

```html
<!DOCTYPE html>
<html lang="en">
<head>
<meta charset="utf-8">
<title>Belvanti Contracting PTY LTD – Business Card</title>
<link rel="stylesheet" href="https://fonts.googleapis.com/css2?family=Roboto+Condensed:wght@700&family=Arimo:wght@400;700&family=Roboto:wght@300&display=swap">
<style>
  :root {
    --backdrop: #3a3a3a;
    --card-white: #f4f5f4;
    --brand-red: #d11a27;
    --brand-red-deep: #680008;
    --swoosh-grey: #9a9b9d;
    --ink: #111111;
    --text-light: #ffffff;
  }
  html, body {
    margin: 0;
    padding: 0;
    width: 1200px;
    height: 999px;
    overflow: hidden;
    background: var(--backdrop);
  }
  .card {
    position: absolute;
    left: 75px;
    top: 199px;
    width: 1050px;
    height: 600px;
    background: var(--card-white);
    overflow: hidden;
  }
  .card-art {
    position: absolute;
    inset: 0;
    width: 1050px;
    height: 600px;
  }
  .company-name {
    position: absolute;
    top: 38px;
    left: 0;
    width: 1050px;
    margin: 0;
    text-align: center;
    color: var(--text-light);
    font-family: "Roboto Condensed", "Arial Narrow", sans-serif;
    font-weight: 700;
    font-size: 76px;
    line-height: 1;
    letter-spacing: 0.5px;
    white-space: nowrap;
  }
  .company-name .suffix {
    font-size: 32px;
    margin-left: 8px;
  }
  .slogan {
    position: absolute;
    top: 142px;
    left: 0;
    width: 1050px;
    margin: 0;
    text-align: center;
    color: var(--text-light);
    font-family: "Arimo", Arial, sans-serif;
    font-weight: 700;
    font-size: 36px;
    line-height: 1;
    white-space: nowrap;
  }
  .services {
    position: absolute;
    top: 313px;
    left: 0;
    width: 1050px;
    margin: 0;
    text-align: center;
    color: var(--ink);
    font-family: "Roboto", Helvetica, sans-serif;
    font-weight: 300;
    font-size: 28px;
    line-height: 40px;
  }
  .contact {
    position: absolute;
    top: 466px;
    left: 0;
    width: 1050px;
    margin: 0;
    text-align: center;
    color: var(--ink);
    font-family: "Arimo", Arial, sans-serif;
    font-weight: 700;
    font-size: 68px;
    line-height: 1;
    letter-spacing: -1px;
    white-space: nowrap;
  }
</style>
</head>
<body>
  <section class="card">
    <svg class="card-art" viewBox="0 0 1050 600" aria-hidden="true">
      <defs>
        <linearGradient id="header-red" x1="0" y1="0" x2="0" y2="1">
          <stop offset="0" stop-color="var(--brand-red)" />
          <stop offset="1" stop-color="var(--brand-red-deep)" />
        </linearGradient>
      </defs>
      <rect class="header-band" x="0" y="0" width="1050" height="250" fill="url(#header-red)" />
      <path class="swoosh" d="M0,246 C200,216 440,204 630,212 C430,213 200,236 0,276 Z" fill="var(--swoosh-grey)" />
      <path class="card-body" d="M0,276 C200,236 430,213 630,212 C800,211 950,225 1050,246 V600 H0 Z" fill="var(--card-white)" />
    </svg>

    <h1 class="company-name">BELVANTI CONTRACTING<span class="suffix">PTY LTD</span></h1>
    <p class="slogan">WHERE NOT FAZED WE WILL LAY ANYTHING</p>
    <p class="services">Pit and Pipe installations Trenching,Excavations, concreting civil works,<br>over thirty years experiance</p>
    <p class="contact">Glen 0491536208</p>
  </section>
</body>
</html>
```